Lumoxra - Web Design Project

I am looking for a 5 page design.
I would like it to be like the design of this site: www.quarvelle.com.
Which means it can be all one page effectively. With quick scroll tabs at the top.
I would like it to include parallax scrolling (The parallax effect uses multiple backgrounds which seem to move at different speeds to create a sensation of depth (creating a faux-3D effect)).
I have uploaded my logo. I would like this to be used in the site design.
I would like the site design to include 3D DNA creative.
Please note the PixHaven photos attached do not belong to me they are purely to inspire creative ideas. However I would be more than happy to purchase these photos to use if the designer thought this would be beneficial.
Must have
- parallax scrolling
DNA pictures (3D effect)
Please use site for reference: www.quarvelle.com
Use at least 1 of the logos in design...

```html
<!DOCTYPE html>
<html lang="en">
<head>
<meta charset="utf-8">
<title>Lumoxra – DNA Research Centre</title>
<link href="https://fonts.googleapis.com/css2?family=Open+Sans:wght@400;600&family=Ubuntu:wght@400;500&display=swap" rel="stylesheet">
<style>
:root{
  --header-bg:#ebebeb;
  --nav-text:#3a3a3a;
  --logo-navy:#1f2a4a;
  --bar-dark:#2a2a2a;
  --bar-light:#8a8a8a;
  --hero-deep:#06121c;
  --hero-mid:#1d5570;
  --hero-light:#8fc4d6;
  --about-deep:#052a6a;
  --about-mid:#0a4ea0;
  --about-cyan:#1fb6d6;
  --panel:#061a33;
  --services-deep:#02143d;
  --services-mid:#0a4fb8;
  --services-glow:#3aa2f0;
  --footer-bg:#1c1c1c;
  --footer-text:#cfcfcf;
  --white:#ffffff;
}
*{margin:0;padding:0;box-sizing:border-box}
html,body{width:795px;height:1200px;overflow:hidden}
body{position:relative;font-family:"Open Sans",Arial,sans-serif;color:var(--white);background:var(--header-bg)}
.abs{position:absolute}

/* header */
.site-header{left:0;top:0;width:795px;height:130px;background:var(--header-bg)}
.brand{left:145px;top:52px;display:flex;align-items:center;gap:8px}
.brand-mark{width:22px;height:22px;border-radius:50%;background:var(--logo-navy)}
.brand-name{font-family:"Ubuntu",sans-serif;font-size:18px;letter-spacing:3px;color:var(--logo-navy);text-transform:uppercase}
.search{left:540px;top:70px;width:124px;height:16px;background:#f6f6f6;border:1px solid #dedede}
.search span{position:absolute;left:6px;top:2px;font-size:6px;color:#bbb}
.search svg{position:absolute;right:4px;top:2px}
.main-nav{top:102px;left:0;font-size:8.5px;color:var(--nav-text);letter-spacing:.2px}
.main-nav a{position:absolute;white-space:nowrap;text-decoration:none;color:inherit}
.header-rule{left:0;top:130px;width:795px;height:4px;background:var(--bar-dark)}
.header-rule::after{content:"";position:absolute;left:549px;top:0;width:246px;height:4px;background:var(--bar-light)}

/* hero */
.hero{left:0;top:134px;width:795px;height:329px;
  background:
    radial-gradient(ellipse 120px 150px at 330px 150px,rgba(90,190,230,.75),transparent 70%),
    radial-gradient(ellipse 260px 120px at 600px 170px,rgba(170,205,220,.55),transparent 70%),
    radial-gradient(ellipse 200px 140px at 180px 70px,rgba(120,170,190,.45),transparent 70%),
    radial-gradient(ellipse 160px 110px at 720px 260px,rgba(150,190,205,.4),transparent 70%),
    radial-gradient(ellipse at 40% 50%,var(--hero-mid) 0%,var(--hero-deep) 70%),
    var(--hero-deep)}
.hero-arrow{width:36px;height:36px;border-radius:50%;background:#111;top:280px}
.hero-arrow svg{position:absolute;left:11px;top:10px}
.hero-title{left:152px;top:282px;font-family:"Ubuntu",sans-serif;font-size:26px;font-weight:400}
.hero-sub{left:152px;top:320px;font-family:"Ubuntu",sans-serif;font-size:15.5px}

/* about */
.about{left:0;top:463px;width:795px;height:341px;
  background:linear-gradient(100deg,var(--about-deep) 0%,#0a3f8c 45%,var(--about-mid) 60%,var(--about-cyan) 100%)}
.about-art{left:440px;top:463px;width:355px;height:341px;
  background:
    radial-gradient(ellipse 60px 150px at 160px 190px,rgba(80,230,250,.6),transparent 70%),
    radial-gradient(ellipse at 50% 65%,rgba(60,220,240,.45),transparent 65%)}
.section-title{font-family:"Ubuntu",sans-serif;font-size:27px;font-weight:500}
.about-title{left:133px;top:520px}
.about-sub{left:133px;top:552px;font-family:"Ubuntu",sans-serif;font-size:13.5px;letter-spacing:4px}
.about-panel{left:131px;top:602px;width:345px;height:119px;background:var(--panel);padding:20px 23px 0}
.about-panel p{font-size:6.6px;line-height:12.4px;text-align:justify}
.read-more{left:423px;top:729px;font-size:7.5px;font-weight:600}

/* services */
.services{left:0;top:804px;width:795px;height:336px;
  background:
    radial-gradient(ellipse 220px 180px at 600px 250px,rgba(80,180,255,.6),transparent 70%),
    radial-gradient(ellipse 160px 200px at 120px 150px,rgba(30,110,220,.5),transparent 70%),
    radial-gradient(ellipse at 70% 70%,var(--services-glow) 0%,var(--services-mid) 35%,var(--services-deep) 80%)}
.services-title{left:130px;top:828px}
.services-intro{left:131px;top:882px;width:534px;font-size:7.4px;line-height:11.3px;text-align:justify}
.card{top:953px;width:125px}
.card-img{height:82px}
.card-label{margin-top:14px;text-align:center;font-size:9.5px;line-height:12px}
.dots{left:374px;top:1082px;display:flex;gap:4px}
.dots i{width:9px;height:9px;border-radius:50%;background:#666}
.dots i:first-child{background:var(--white)}

/* footer */
.site-footer{left:0;top:1140px;width:795px;height:60px;background:var(--footer-bg);color:var(--footer-text)}
.footer-links{left:129px;top:19px;font-size:6.3px;word-spacing:1px}
.footer-legal{left:129px;top:34px;font-size:6.3px}
.social{left:572px;top:19px;display:flex;gap:4px}
.social i{width:20px;height:20px;border-radius:50%;background:var(--white)}
</style>
</head>
<body>

<header class="site-header abs">
  <div class="brand abs"><span class="brand-mark"></span><span class="brand-name">Lumoxra</span></div>
  <div class="search abs"><span>Search</span>
    <svg width="11" height="11" viewBox="0 0 11 11"><circle cx="4" cy="4" r="3" fill="none" stroke="#444" stroke-width="1.3"/><line x1="6.2" y1="6.2" x2="10" y2="10" stroke="#444" stroke-width="1.6"/></svg>
  </div>
  <nav class="main-nav abs">
    <a style="left:279px">HOME</a>
    <a style="left:325px">ABOUT US</a>
    <a style="left:386px">SERVICES</a>
    <a style="left:444px">PRODUCTS</a>
    <a style="left:508px">RESEARCH</a>
    <a style="left:573px">EVENTS</a>
    <a style="left:625px">CONTACT</a>
  </nav>
</header>
<div class="header-rule abs"></div>

<section class="hero abs" role="img" aria-label="Futuristic 3D DNA strand held by a robotic hand with glowing interface graphics"></section>
<div class="hero-arrow abs" style="left:87px"><svg width="14" height="16" viewBox="0 0 14 16"><polyline points="10,2 4,8 10,14" fill="none" stroke="#fff" stroke-width="2.4"/></svg></div>
<div class="hero-arrow abs" style="left:670px"><svg width="14" height="16" viewBox="0 0 14 16"><polyline points="4,2 10,8 4,14" fill="none" stroke="#fff" stroke-width="2.4"/></svg></div>
<h1 class="hero-title abs">Lumoxra</h1>
<p class="hero-sub abs">A DNA Reasearch Centre</p>

<section class="about abs"></section>
<div class="about-art abs" role="img" aria-label="Glowing blue 3D DNA double helix with data text"></div>
<h2 class="section-title about-title abs">About Lumoxra</h2>
<p class="about-sub abs">DNA Research centre</p>
<div class="about-panel abs">
  <p>DNA Research Centre is an autonomous registered research organization, which provides services and training in Biotechnology, Bioinformatics, Clinical Research &amp; Forensic Science. LDRC works to create a platform conductive for the growth promotion and partnering in Life Sciences field. We at LDRC are dedicated to provide a backbone to the Genome valley, for proper utilization of the advancements in the field of biological sciences by taking together Govt and Private sector organizations, Companies, professionals, academicians and students through consultative, advisory, educative process.</p>
</div>
<a class="read-more abs">Read More ...</a>

<section class="services abs" role="img" aria-label="Blue digital background of glowing DNA sequence data"></section>
<h2 class="section-title services-title abs">Services</h2>
<p class="services-intro abs">Lorem Ipsum is simply dummy text of the printing and typesetting industry. Lorem Ipsum has been the industry's standard dummy text ever since the 1500s, when an unknown printer took a galley of type and scrambled it to make a type specimen book. It has survived not only five centuries, but also the leap into electronic typesetting, remaining essentially unchanged. It was popularised in the 1960s with the release of Transet sheets containing Lorem Ipsum passages, and more recently with desktop publishing software like Folio Layout including versions of Lorem Ipsum.</p>

<div class="card abs" style="left:130px">
  <div class="card-img" role="img" aria-label="Gloved hand holding a green sample vial over sequencing data" style="background:radial-gradient(ellipse 18px 30px at 88px 35px,rgba(80,220,90,.9),transparent 75%),linear-gradient(160deg,#0d2a66,#2f6fd6 45%,#0e3a8a 70%,#c9d6e6)"></div>
  <p class="card-label">Forensic Services</p>
</div>
<div class="card abs" style="left:267px">
  <div class="card-img" role="img" aria-label="Lab technician in mask and gloves pipetting a sample" style="background:radial-gradient(ellipse 40px 45px at 55px 40px,rgba(150,210,225,.9),transparent 75%),linear-gradient(135deg,#f2f5f6,#c6dde6 45%,#5a9ec0 80%,#2d5f9a)"></div>
  <p class="card-label">Private DNA Testing</p>
</div>
<div class="card abs" style="left:403px">
  <div class="card-img" role="img" aria-label="Pale blue DNA helix over genetic code" style="background:linear-gradient(135deg,#cfe8f2,#92c6dc 50%,#5d9fc0 80%,#3f7ea6)"></div>
  <p class="card-label">Genetic Compatibility<br>DNA Test</p>
</div>
<div class="card abs" style="left:539px">
  <div class="card-img" role="img" aria-label="Scientist examining a plant sample in a test tube" style="background:radial-gradient(ellipse 14px 38px at 102px 42px,rgba(200,220,180,.8),transparent 75%),linear-gradient(120deg,#c9a892,#e8ddd4 40%,#f4f1ee 65%,#c7d2d6)"></div>
  <p class="card-label">Plant DNA Test</p>
</div>
<div class="dots abs"><i></i><i></i><i></i><i></i></div>

<footer class="site-footer abs">
  <p class="footer-links abs">Home &nbsp;| &nbsp;about us &nbsp;| &nbsp;Services &nbsp;| &nbsp;Products &nbsp;| &nbsp;Research &nbsp;| &nbsp;Events &nbsp;| &nbsp;Contact3</p>
  <p class="footer-legal abs">© Lumoxra 2013 &nbsp;&nbsp;| &nbsp;Privacy Policy &nbsp;| Terms &amp; conditions</p>
  <div class="social abs"><i></i><i></i><i></i><i></i></div>
</footer>

</body>
</html>
```